Design for a real estate wev portal

Contents and features of the site
---------------------------------
Website in 5 languages: French, Dutch, English, German, Spanish.
English name of the site: Lantern Nest Place
Main purpose of the site:
- allow people to rent their house/ appartment for flatsharing purposes.
- help people wanting to find a room in flatsharing
- help people to find additional roommates for their flatsharing
Key interaction sequence:
1. I create a "group" of people who have common interest/hobbies
2. People who have the same interests/hobbies join my group
3. I look for a house/appartment to host my group
Website structure will be the following:
- Home
- Groups
-- Look for a group
--- Join a group
-- Create a group
- Properties
-- Look for a house/appartement
-- Apply
- Sales conditions
- Contact
- My account
-- My profile
-- My groups OR my properties
Your mission
------------
The client has no graphical guidelines, simply a logo (see attached).
We need a (responsive compliant) design for the following pages (we expect PSD's from you. No HTML nor CSS):
1. homepage (see example and wireframe attached)
2. properties search result list (see wireframe attached)
3. "detailed" form for properties
4. groups search result list
5. "detailed" form for groups
6. my account page
FOR THE COMPETITION step we only expect from you the design of first 2 screens.
Based on that, we will select the designer who will win the project, and will have to design the 4 remaining screens.
Target Market(s)
B2C
Industry/Entity Type
Real Estate
Number of Pages Required
5+ page
Look and feel
Each slider illustrates characteristics of the customer's brand and the style your logo design should communicate.

```html
<!DOCTYPE html>
<html lang="en">
<head>
<meta charset="utf-8">
<title>Lantern Nest Place – Properties</title>
<link href="https://fonts.googleapis.com/css2?family=Dosis:wght@400;500;600;700&display=swap" rel="stylesheet">
<style>
:root{
  --teal:#1a9fb1;
  --green:#6cbf43;
  --ink:#3a3a3a;
  --muted:#666;
  --line:#dedede;
  --white:#fff;
}
*{box-sizing:border-box;margin:0;padding:0}
html,body{width:1155px;height:1200px;overflow:hidden;background:var(--white)}
body{font-family:"Dosis",sans-serif;color:var(--ink);position:relative;font-size:10px}
.abs{position:absolute}
.top-band{left:0;top:0;width:1155px;height:4px;background:var(--green)}
.header{left:0;top:4px;width:1155px;height:123px;background:var(--white);border-bottom:1px solid #e6e6e6;z-index:2}
.main-nav{left:235px;top:0;width:201px;height:123px;background:var(--teal);z-index:3}
.main-nav a{position:absolute;color:#fff;font-weight:600;font-size:10px;text-decoration:none;text-transform:uppercase;letter-spacing:.2px;white-space:nowrap}
.main-nav a.active{border-bottom:1px solid #fff;padding-bottom:1px}
.caret{font-size:7px;margin-left:3px}
.submenu{left:386px;top:116px;height:48px;background:var(--green);z-index:4;padding:8px 12px 0 13px;white-space:nowrap}
.submenu::before{content:"";position:absolute;left:8px;top:-6px;border:6px solid transparent;border-bottom-color:var(--green);border-top:0}
.submenu a{display:block;color:#fff;font-weight:600;font-size:9.5px;text-decoration:none;line-height:19px;text-transform:uppercase}
.brand{left:492px;top:42px;display:flex;align-items:center;gap:8px;z-index:3}
.brand-dot{width:14px;height:14px;border-radius:50%;background:var(--green)}
.brand-name{font-size:25px;font-weight:600;color:#333;letter-spacing:.5px}
.auth{top:14px;height:22px;font-size:9.5px;font-weight:500;text-transform:uppercase;display:flex;align-items:center;justify-content:center;z-index:3}
.register{left:792px;width:78px;border:1px solid #cfcfcf;color:#555;background:#fff}
.login{left:875px;width:46px;background:var(--teal);color:#fff}
.backdrop{left:0;top:127px;width:1155px;height:849px;background:linear-gradient(180deg,#f7f7f7 0%,#e7e7e7 55%,#dcdcdc 100%)}
.panel{background:var(--white);border:1px solid #e8e8e8}
.sidebar{left:235px;top:146px;width:155px;height:811px}
.content{left:401px;top:146px;width:519px;height:811px}
.s-title{font-weight:600;font-size:11.5px;text-transform:uppercase;color:#444}
.label{font-size:9.5px;color:#555}
.field{border:1px solid var(--line);background:#fff;font-size:9.5px;color:#666;display:flex;align-items:center;justify-content:center;white-space:nowrap}
.search{justify-content:flex-start;padding-left:8px;gap:5px;color:#999}
.radio{display:flex;align-items:center;gap:7px;font-size:9.5px;color:#555}
.radio i{width:10px;height:10px;border-radius:50%;border:1px solid #ddd;display:inline-block;position:relative;background:#f7f7f7}
.radio i.on::after{content:"";position:absolute;left:2px;top:2px;width:4px;height:4px;border-radius:50%;background:var(--teal)}
.cta{background:var(--teal);color:#fff;font-weight:600;font-size:11px;display:flex;align-items:center;justify-content:center}
.basic p{font-size:9.5px;line-height:13.5px;color:#555}
.results-head{font-size:11px;font-weight:600;color:#444;white-space:nowrap}
.card{left:17px;width:484px;height:164px;border:1px solid #e3e3e3;background:#fff}
.photo{left:14px;top:10px;width:218px;height:144px}
.play{left:96px;top:59px;width:30px;height:30px;border:2px solid rgba(255,255,255,.85);border-radius:50%}
.price{left:11px;top:14px;height:28px;padding:0 5px 0 8px;background:var(--teal);color:#fff;font-size:15px;font-weight:500;display:flex;align-items:baseline;padding-top:4px}
.price small{font-size:7px;margin-left:1px}
.addr{left:246px;top:13px;display:flex;align-items:center;gap:5px;font-size:14px;color:#444;white-space:nowrap}
.badge{left:246px;top:38px;width:87px;height:20px;background:var(--teal);color:#fff;font-size:9.5px;display:flex;align-items:center;justify-content:center}
.meta{font-size:9.5px;color:#555;white-space:nowrap}
.meta.it{font-style:italic;color:#777}
.desc{left:246px;top:93px;width:232px;font-size:9.5px;line-height:14.5px;color:#555}
.desc b{color:#333;font-weight:700;display:block;white-space:nowrap;overflow:hidden}
.icons{left:246px;top:143px;display:flex;gap:6px}
.footer{left:0;top:976px;width:1155px;height:220px;background:#f4f4f4;border-top:1px solid #e3e3e3}
.f-title{font-size:11px;font-weight:700;color:#333;text-transform:uppercase}
.f-text{font-size:9.5px;line-height:16px;color:#555}
.f-list{list-style:none;font-size:9.5px;color:#555;line-height:17px;white-space:nowrap}
.f-list li::before{content:"›";margin-right:5px;color:#777}
.f-rule{left:235px;top:1156px;width:686px;height:1px;background:#bdbdbd}
.copy{left:235px;top:1166px;font-size:11px;color:#555}
.bottom-band{left:0;top:1196px;width:1155px;height:4px;background:var(--green)}
</style>
</head>
<body>
<div class="abs top-band"></div>

<header class="abs header">
  <nav class="abs main-nav">
    <a style="left:22px;top:41px">Home</a>
    <a style="left:98px;top:41px">Sales conditions</a>
    <a style="left:20px;top:67px">Groups<span class="caret">⌄</span></a>
    <a style="left:98px;top:67px">Contact</a>
    <a style="left:20px;top:93px">Properties<span class="caret">⌄</span></a>
    <a class="active" style="left:98px;top:93px">My account<span class="caret">⌄</span></a>
  </nav>
  <div class="abs brand"><span class="brand-dot"></span><span class="brand-name">Lantern Nest Place</span></div>
  <div class="abs auth register">Register here</div>
  <div class="abs auth login">Login</div>
</header>
<div class="abs submenu">
  <a>My profile</a>
  <a>My groups or my properties</a>
</div>

<div class="abs backdrop" role="img" aria-label="Faint grey photo of a tall building rising behind the page"></div>

<aside class="abs panel sidebar">
  <div class="abs s-title" style="left:11px;top:14px">Votre recherche:</div>
  <div class="abs field search" style="left:11px;top:34px;width:133px;height:24px">
    <svg width="9" height="9" viewBox="0 0 10 10"><circle cx="4" cy="4" r="3.2" fill="none" stroke="#aaa"/><path d="M6.5 6.5L9.5 9.5" stroke="#aaa"/></svg>Ou cherchez-vous?
  </div>
  <div class="abs label" style="left:11px;top:79px">Perimetre de recherche:</div>
  <div class="abs" style="left:11px;top:96px;width:130px;height:3px;background:#ddd"></div>
  <div class="abs" style="left:11px;top:96px;width:82px;height:3px;background:var(--teal)"></div>
  <svg class="abs" style="left:88px;top:97px" width="10" height="10" viewBox="0 0 10 10"><path d="M5 0v7M2 5l3 3 3-3" stroke="#1a9fb1" stroke-width="1.6" fill="none"/></svg>
  <div class="abs" style="left:83px;top:107px;font-size:9.5px;font-style:italic;color:var(--teal)">20km</div>

  <div class="abs label" style="left:11px;top:133px">Loyer par mois</div>
  <div class="abs field" style="left:11px;top:152px;width:78px;height:24px">Min</div>
  <div class="abs field" style="left:94px;top:152px;width:51px;height:24px">500</div>

  <div class="abs label" style="left:11px;top:191px">Type de logement</div>
  <div class="abs field" style="left:11px;top:210px;width:66px;height:24px">Maison</div>
  <div class="abs field" style="left:81px;top:210px;width:64px;height:24px">Appartement</div>

  <div class="abs label" style="left:11px;top:248px">Chambres Disponibles</div>
  <div class="abs field" style="left:11px;top:268px;width:29px;height:24px">1</div>
  <div class="abs field" style="left:39px;top:268px;width:31px;height:24px">2</div>
  <div class="abs field" style="left:69px;top:268px;width:35px;height:24px">3</div>
  <div class="abs field" style="left:103px;top:268px;width:42px;height:24px">4</div>

  <div class="abs radio" style="left:11px;top:305px"><i class="on"></i>Annonces avec photo</div>
  <div class="abs radio" style="left:11px;top:325px"><i></i>Chambres Doubles</div>
  <div class="abs radio" style="left:11px;top:345px"><i class="on"></i>Meubles</div>
  <div class="abs radio" style="left:11px;top:365px"><i></i>Courte Duree</div>

  <div class="abs label" style="left:11px;top:395px">Age du Colocataire</div>
  <div class="abs field" style="left:11px;top:415px;width:78px;height:24px">35 ⌄</div>
  <div class="abs field" style="left:94px;top:415px;width:51px;height:24px">40 ⌄</div>

  <div class="abs label" style="left:11px;top:453px">Sexe du Colocataire</div>
  <div class="abs field" style="left:11px;top:473px;width:66px;height:24px">Homme</div>
  <div class="abs field" style="left:81px;top:473px;width:64px;height:24px">Femme</div>

  <div class="abs label" style="left:11px;top:511px">Situation du Colocataire</div>
  <div class="abs field" style="left:11px;top:530px;width:66px;height:24px">Edudiant</div>
  <div class="abs field" style="left:81px;top:530px;width:64px;height:24px">Salarie</div>

  <div class="abs" style="left:6px;top:580px;width:143px;height:3px;background:#e2e2e2"></div>

  <div class="abs" style="left:11px;top:603px;display:flex;align-items:center;gap:6px">
    <svg width="14" height="14" viewBox="0 0 14 14"><circle cx="7" cy="4.5" r="3" fill="none" stroke="#666"/><path d="M1.5 13c.5-3.5 2.8-5 5.5-5s5 1.5 5.5 5z" fill="none" stroke="#666"/></svg>
    <span class="s-title" style="font-size:11px">Membre Basique</span>
  </div>
  <div class="abs basic" style="left:11px;top:630px;width:136px">
    <p>Lorem ipsum dolor sit amet, consectetur adipisicing elit, sed do eiusmod tempor</p>
    <p style="margin-top:13px">incididunt ut labore et dolore magna aliqua. Ut enim ad minim veniam, quis nostrud exercitation ullamco laboris nisi ut aliquip ex ea commodo</p>
  </div>
  <div class="abs cta" style="left:11px;top:764px;width:126px;height:31px">Activer un pass</div>
</aside>

<main class="abs panel content">
  <div class="abs results-head" style="left:18px;top:20px">6 offres de colocation a paris-ile De France</div>
  <div class="abs label" style="left:346px;top:16px">Trier par</div>
  <div class="abs field" style="left:390px;top:9px;width:111px;height:25px;justify-content:space-between;padding:0 10px">Plus recent<span>⌄</span></div>

  <article class="abs card" style="top:52px">
    <div class="abs photo" role="img" aria-label="Photo of a tall yellow apartment tower under a blue sky" style="background:linear-gradient(160deg,#4d84c8 0%,#a9c2de 40%,#d9b86a 70%,#4f6b3a 100%)"><div class="abs play"></div></div>
    <div class="abs price">€500<small>/Mois</small></div>
    <div class="abs addr"><svg width="13" height="16" viewBox="0 0 13 16"><path d="M6.5 15S1 9.5 1 6a5.5 5.5 0 0 1 11 0c0 3.5-5.5 9-5.5 9z" fill="none" stroke="#888"/><circle cx="6.5" cy="6" r="2" fill="none" stroke="#888"/></svg>Allee Des Peupliers, Montreuil...</div>
    <div class="abs badge">Membre Premium</div>
    <div class="abs meta" style="left:349px;top:42px">Mis a jour il y a 1 jour</div>
    <div class="abs meta it" style="left:246px;top:67px">Disponible le 26 dec.</div>
    <div class="abs meta it" style="left:340px;top:67px">Non specifie</div>
    <div class="abs desc"><b>Appartement loue meuble de 3ch, 100m2 a 5min a pie...</b>Bonjour, Je propose a partir du mois de decembre mon appartement libre pour en faire une colocation meublee.Il</div>
    <div class="abs icons"><svg width="11" height="10" viewBox="0 0 11 10"><rect x=".5" y=".5" width="10" height="9" fill="none" stroke="#777"/><path d="M1 8l3-3 2 2 2-2 2 2" fill="none" stroke="#777"/></svg><svg width="11" height="10" viewBox="0 0 11 10"><path d="M.5 4.5l10-4-3 9-2-3.5z" fill="none" stroke="#777"/></svg></div>
  </article>

  <article class="abs card" style="top:224px">
    <div class="abs photo" role="img" aria-label="Photo of a yellow family house with a lawn and a for-sale sign" style="background:linear-gradient(170deg,#5f95d0 0%,#b9d0e6 30%,#c79a4a 55%,#5e8f2f 100%)"><div class="abs play"></div></div>
    <div class="abs price">€500<small>/Mois</small></div>
    <div class="abs addr"><svg width="13" height="16" viewBox="0 0 13 16"><path d="M6.5 15S1 9.5 1 6a5.5 5.5 0 0 1 11 0c0 3.5-5.5 9-5.5 9z" fill="none" stroke="#888"/><circle cx="6.5" cy="6" r="2" fill="none" stroke="#888"/></svg>Allee Des Peupliers, Montreuil...</div>
    <div class="abs badge">Membre Premium</div>
    <div class="abs meta" style="left:349px;top:42px">Mis a jour il y a 1 jour</div>
    <div class="abs meta it" style="left:246px;top:67px">Disponible le 26 dec.</div>
    <div class="abs meta it" style="left:340px;top:67px">Non specifie</div>
    <div class="abs desc"><b>Appartement loue meuble de 3ch, 100m2 a 5min a pie...</b>Bonjour, Je propose a partir du mois de decembre mon appartement libre pour en faire une colocation meublee.Il</div>
    <div class="abs icons"><svg width="11" height="10" viewBox="0 0 11 10"><rect x=".5" y=".5" width="10" height="9" fill="none" stroke="#777"/><path d="M1 8l3-3 2 2 2-2 2 2" fill="none" stroke="#777"/></svg><svg width="11" height="10" viewBox="0 0 11 10"><path d="M.5 4.5l10-4-3 9-2-3.5z" fill="none" stroke="#777"/></svg></div>
  </article>

  <article class="abs card" style="top:398px">
    <div class="abs photo" role="img" aria-label="Photo of a city skyline seen from a balcony with red flowers" style="background:linear-gradient(180deg,#e4e7ea 0%,#b7bcc2 45%,#c4503a 75%,#3f6b2c 100%)"><div class="abs play"></div></div>
    <div class="abs price">€500<small>/Mois</small></div>
    <div class="abs addr"><svg width="13" height="16" viewBox="0 0 13 16"><path d="M6.5 15S1 9.5 1 6a5.5 5.5 0 0 1 11 0c0 3.5-5.5 9-5.5 9z" fill="none" stroke="#888"/><circle cx="6.5" cy="6" r="2" fill="none" stroke="#888"/></svg>Allee Des Peupliers, Montreuil...</div>
    <div class="abs badge">Membre Premium</div>
    <div class="abs meta" style="left:349px;top:42px">Mis a jour il y a 1 jour</div>
    <div class="abs meta it" style="left:246px;top:67px">Disponible le 26 dec.</div>
    <div class="abs meta it" style="left:340px;top:67px">Non specifie</div>
    <div class="abs desc"><b>Appartement loue meuble de 3ch, 100m2 a 5min a pie...</b>Bonjour, Je propose a partir du mois de decembre mon appartement libre pour en faire une colocation meublee.Il</div>
    <div class="abs icons"><svg width="11" height="10" viewBox="0 0 11 10"><rect x=".5" y=".5" width="10" height="9" fill="none" stroke="#777"/><path d="M1 8l3-3 2 2 2-2 2 2" fill="none" stroke="#777"/></svg><svg width="11" height="10" viewBox="0 0 11 10"><path d="M.5 4.5l10-4-3 9-2-3.5z" fill="none" stroke="#777"/></svg></div>
  </article>

  <article class="abs card" style="top:570px">
    <div class="abs photo" role="img" aria-label="Photo of a white suburban house with a red for-sale sign" style="background:linear-gradient(160deg,#6a9dd4 0%,#d8dde2 40%,#c9c2b0 65%,#b83a34 85%,#5d7a3a 100%)"><div class="abs play"></div></div>
    <div class="abs price">€500<small>/Mois</small></div>
    <div class="abs addr"><svg width="13" height="16" viewBox="0 0 13 16"><path d="M6.5 15S1 9.5 1 6a5.5 5.5 0 0 1 11 0c0 3.5-5.5 9-5.5 9z" fill="none" stroke="#888"/><circle cx="6.5" cy="6" r="2" fill="none" stroke="#888"/></svg>Allee Des Peupliers, Montreuil...</div>
    <div class="abs badge">Membre Premium</div>
    <div class="abs meta" style="left:349px;top:42px">Mis a jour il y a 1 jour</div>
    <div class="abs meta it" style="left:246px;top:67px">Disponible le 26 dec.</div>
    <div class="abs meta it" style="left:340px;top:67px">Non specifie</div>
    <div class="abs desc"><b>Appartement loue meuble de 3ch, 100m2 a 5min a pie...</b>Bonjour, Je propose a partir du mois de decembre mon appartement libre pour en faire une colocation meublee.Il</div>
    <div class="abs icons"><svg width="11" height="10" viewBox="0 0 11 10"><rect x=".5" y=".5" width="10" height="9" fill="none" stroke="#777"/><path d="M1 8l3-3 2 2 2-2 2 2" fill="none" stroke="#777"/></svg><svg width="11" height="10" viewBox="0 0 11 10"><path d="M.5 4.5l10-4-3 9-2-3.5z" fill="none" stroke="#777"/></svg></div>
  </article>
</main>

<footer class="abs footer">
  <div class="abs f-title" style="left:235px;top:46px">About Lantern Nest</div>
  <p class="abs f-text" style="left:238px;top:72px;width:200px">Lorem ipsum dolor sit amet, consectetur adipisicing elit, sed do eiusmod tempor incididunt ut labore et dolore magna aliqua. Ut enim ad minim veniam, quis nostrud exercitation ullamco laboris nisi ut aliquip ex ea commodo consequat.</p>

  <div class="abs f-title" style="left:466px;top:46px">Quick links</div>
  <ul class="abs f-list" style="left:466px;top:72px">
    <li>Single Family</li><li>New construction</li><li>On rent</li><li>On sale</li>
  </ul>
  <ul class="abs f-list" style="left:550px;top:72px">
    <li>Single Family</li><li>New construction</li><li>On rent</li><li>On sale</li>
  </ul>

  <div class="abs f-title" style="left:645px;top:46px">Latest info</div>
  <ul class="abs f-list" style="left:645px;top:72px;width:140px;line-height:13px;white-space:normal">
    <li style="margin-bottom:5px">Lorem ipsum dolor sit amet, consectetur adipisicing</li>
    <li style="margin-bottom:5px">Lorem ipsum dolor sit amet, consectetur</li>
    <li>adipisicing elit, sed do eiusmod tempor incididunt</li>
  </ul>

  <div class="abs f-title" style="left:798px;top:46px">Address</div>
  <svg class="abs" style="left:798px;top:74px" width="10" height="13" viewBox="0 0 10 13"><path d="M5 12S1 7.5 1 4.8a4 4 0 0 1 8 0C9 7.5 5 12 5 12z" fill="none" stroke="#666"/><circle cx="5" cy="4.8" r="1.5" fill="none" stroke="#666"/></svg>
  <p class="abs f-text" style="left:815px;top:70px;width:110px;line-height:14.5px">niam, quis nostrud exercitn lamco laboris nisi ut aliquip ex ea, London</p>
  <svg class="abs" style="left:796px;top:127px" width="14" height="9" viewBox="0 0 14 9"><rect x=".5" y=".5" width="13" height="8" fill="none" stroke="#666"/><path d="M.5 .5l6.5 4.5 6.5-4.5" fill="none" stroke="#666"/></svg>
  <p class="abs f-text" style="left:815px;top:121px">hello@lanternnestplace.com</p>
  <svg class="abs" style="left:797px;top:144px" width="12" height="12" viewBox="0 0 12 12"><circle cx="6" cy="6" r="5.5" fill="none" stroke="#666"/><path d="M4 3.5c0 2.5 2 4.5 4.5 4.5" fill="none" stroke="#666"/></svg>
  <p class="abs f-text" style="left:815px;top:140px">+16541 2200 4800</p>
</footer>
<div class="abs f-rule"></div>
<div class="abs copy">@All right reserved by the company 2015.</div>
<div class="abs bottom-band"></div>
</body>
</html>
```